iOS App Design Project for Pebble Tasks

We are looking for a redesign of the UI for our app, Pebble Tasks. The app is a to-do list type app with 4 screens, and we already have a UI for it but we would like a nicer looking one that has a better colour scheme and is more intuitive.

We would like something that is a real treat to look at, and that users really want to use. Essentially what we want is the nicest and most simple design possible, as the current UI we have is not very user friendly.

The app is already on the market and is free so if you have an iOS device you can download it and take a look at it, and we have also included screenshots of the app.
Updates

Project Deadline Extended
Reason: I am updating the design brief and will also guarantee the payment.

Target Market(s)

Mobile users looking for simplicity

Requirements
Must have
• - Very visually pleasing
- Simple layout with minimal clutter
- Icons and buttons that explain what they do
Should not have
• Any features that detract from the simplicity of the app are not wanted.

```html
<!DOCTYPE html>
<html lang="en">
<head>
<meta charset="utf-8">
<title>Pebble Tasks – App Screens</title>
<link href="https://fonts.googleapis.com/css2?family=Arimo:wght@400;700&display=swap" rel="stylesheet">
<style>
:root{
  --stage:#56616b;
  --bar-top:#4a4a4a;
  --bar-bottom:#151515;
  --paper:#f1f0ec;
  --paper-line:#d9d8d2;
  --margin-red:#e7a7a7;
  --ink:#222;
  --tile-edge:#3b3b3b;
  --white:#fff;
  --kb-top:#a8b1bd;
  --kb-bottom:#6f7a8a;
  --blue:#2f7be8;
  --caret:#3d6fe0;
  --field-edge:#a9a9a4;
  --index-ink:#666;
}
*{box-sizing:border-box;margin:0;padding:0}
html,body{width:1200px;height:558px;overflow:hidden}
body{background:var(--stage);font-family:"Arimo",Helvetica,Arial,sans-serif;position:relative;color:var(--ink)}
.screen{position:absolute;top:132px;width:180px;height:268px;background:var(--paper);overflow:hidden;box-shadow:0 4px 14px rgba(0,0,0,.35)}
.screen--home{left:100px}
.screen--list{left:380px}
.screen--new{left:650px}
.screen--notes{left:925px}
.status-bar{position:absolute;top:0;left:0;right:0;height:10px;background:linear-gradient(#d8d8d8,#a9a9a9);color:#111;font-size:6px;font-weight:700;display:flex;align-items:center;padding:0 3px}
.status-bar .carrier{display:flex;align-items:center;gap:2px}
.status-bar .time{position:absolute;left:0;right:0;text-align:center}
.status-bar .battery{margin-left:auto;width:12px;height:6px;border:1px solid #222;border-radius:1px;padding:1px}
.status-bar .battery span{display:block;height:100%;width:100%;background:#3fae3a}
.nav-bar{position:absolute;top:10px;left:0;right:0;height:26px;background:linear-gradient(var(--bar-top),var(--bar-bottom));color:var(--white);display:flex;align-items:center;justify-content:center;border-bottom:1px solid #000}
.nav-title{font-size:11px;font-weight:700}
.nav-btn{position:absolute;top:5px;height:16px;border:1px solid #000;border-radius:3px;background:linear-gradient(#5b5b5b,#222);color:var(--white);font-size:6px;font-weight:700;display:flex;align-items:center;justify-content:center;padding:0 6px}
.nav-btn--back{left:5px;padding-left:8px;clip-path:polygon(6px 0,100% 0,100% 100%,6px 100%,0 50%);border-radius:0 3px 3px 0}
.nav-btn--right{right:5px}
.nav-btn--plus{right:5px;width:16px;padding:0;background:linear-gradient(#f4f4f4,#cfcfcf);color:#111;font-size:13px;line-height:1}
.grid-paper{position:absolute;top:36px;left:0;right:0;bottom:0;background-color:#f3f3f1;background-image:linear-gradient(#e4e4e0 1px,transparent 1px),linear-gradient(90deg,#e4e4e0 1px,transparent 1px);background-size:6px 6px}
.tile{position:absolute;width:59px;height:59px;background:linear-gradient(#2b2b2b,#111);border:1px solid var(--tile-edge);color:var(--white);font-size:7px;display:flex;flex-direction:column;align-items:center;justify-content:flex-end;padding-bottom:6px;gap:6px;box-shadow:0 2px 3px rgba(0,0,0,.3)}
.tile svg{width:24px;height:24px}
.tile--tasks{left:36px;top:27px}
.tile--notes{left:96px;top:87px}
.tile--more{left:36px;top:147px}
.content{position:absolute;top:37px;left:0;right:0;bottom:28px;background:#dcdcd8}
.sheet{position:absolute;left:8px;right:8px;top:7px;bottom:0;background:var(--paper);border:1px solid #c8c8c2;border-bottom:0}
.grocery-list{list-style:none;position:relative}
.grocery-list li{height:20.3px;border-bottom:1px solid var(--paper-line);display:flex;align-items:center;font-size:7px}
.grocery-list .box{width:7px;height:7px;border:1px solid #999;background:#fff;margin:0 12px 0 6px;position:relative}
.grocery-list .box svg{position:absolute;left:0;top:-3px;width:9px;height:9px}
.margin-line{position:absolute;top:0;bottom:0;left:22px;width:1px;background:var(--margin-red)}
.index{position:absolute;right:2px;top:3px;font-size:4.6px;line-height:6.2px;text-align:center;color:var(--index-ink);font-weight:700}
.tab-bar{position:absolute;left:0;right:0;bottom:0;height:28px;background:linear-gradient(#4a4a4a,#111);display:flex;padding:2px 3px}
.tab{flex:1;display:flex;flex-direction:column;align-items:center;justify-content:center;color:#777;font-size:5.5px;gap:1px}
.tab svg{width:12px;height:12px}
.tab--active{background:rgba(255,255,255,.15);border-radius:2px;color:var(--white)}
.form{position:absolute;top:37px;left:0;right:0;height:115px;background:var(--paper)}
.task-field{position:absolute;left:8px;top:5px;width:162px;height:49px;background:#fafaf8;border:1px solid var(--field-edge);border-radius:6px;font-size:9px;line-height:12px;padding:5px 8px}
.caret{display:inline-block;width:1px;height:10px;background:var(--caret);vertical-align:-1px}
.form-row{position:absolute;left:16px;right:10px;display:flex;align-items:center;height:22px}
.form-row--list{top:58px}
.form-row--who{top:83px}
.form-label{width:39px;font-size:8px;font-weight:700}
.form-value{flex:1;height:22px;border:1px solid var(--field-edge);border-radius:5px;background:#fafaf8;font-size:7.5px;display:flex;align-items:center;padding:0 10px;justify-content:space-between}
.chev{color:#777;font-weight:700}
.keyboard{position:absolute;left:0;right:0;bottom:0;height:117px;background:linear-gradient(var(--kb-top),var(--kb-bottom));padding:4px 1px 0}
.key-row{display:flex;justify-content:center;gap:2px;height:21px;margin-bottom:8px}
.key-row:last-child{margin-bottom:0}
.key{width:16px;background:linear-gradient(#fff,#e3e3e3);border-radius:3px;box-shadow:0 1px 0 #4d5563;font-size:10px;font-weight:700;display:flex;align-items:center;justify-content:center}
.key--fn{width:22px;background:linear-gradient(#a4adba,#7f8898);color:var(--white);font-size:7px}
.key--wide{width:42px}
.key--space{width:88px;font-size:7px;font-weight:400;color:#333}
.key--search{width:42px;background:linear-gradient(#5a9bf3,var(--blue));color:var(--white);font-size:7px}
.notes-sheet{position:absolute;left:8px;right:8px;top:3px;bottom:0;background:#eceae5;border:1px solid #c8c8c2;border-bottom:0}
.notes-group{position:absolute;left:3px;right:3px;top:4px;background:var(--paper);border:1px solid #c3c3bd;border-radius:6px;overflow:hidden}
.notes-group li{list-style:none;height:28px;border-bottom:1px solid var(--paper-line);display:flex;align-items:center;justify-content:space-between;padding:0 7px 0 6px;font-size:7.5px;font-weight:700}
.notes-group li.blank{height:90px;border-bottom:0}
</style>
</head>
<body>

<section class="screen screen--home">
  <div class="status-bar"><span class="carrier">▮▮▮ KESTREL</span><span class="time">0:34</span><span class="battery"><span></span></span></div>
  <header class="nav-bar"><h1 class="nav-title">Pebble Tasks</h1></header>
  <div class="grid-paper">
    <div class="tile tile--tasks">
      <svg viewBox="0 0 24 24" fill="none" stroke="#fff" stroke-width="2"><rect x="4" y="4" width="16" height="18" rx="1"/><rect x="8" y="2" width="8" height="4" fill="#fff"/><path d="M8 13l3 3 6-7"/></svg>
      <span>Tasks</span>
    </div>
    <div class="tile tile--notes">
      <svg viewBox="0 0 24 24" fill="none" stroke="#fff" stroke-width="2"><rect x="3" y="5" width="15" height="16"/><path d="M10 15l1-3 9-9 2 2-9 9z" fill="#fff"/></svg>
      <span>Notes</span>
    </div>
    <div class="tile tile--more">
      <svg viewBox="0 0 24 24" fill="none" stroke="#fff" stroke-width="1.5"><rect x="2" y="2" width="20" height="20" stroke-dasharray="3 2"/><path d="M12 7v10M7 12h10" stroke-width="2.5"/></svg>
      <span>More</span>
    </div>
  </div>
</section>

<section class="screen screen--list">
  <div class="status-bar"><span class="carrier">▮▮▮ KESTREL</span><span class="time">0:34</span><span class="battery"><span></span></span></div>
  <header class="nav-bar"><span class="nav-btn nav-btn--back">Back</span><h1 class="nav-title">Groceries</h1><span class="nav-btn nav-btn--plus">+</span></header>
  <div class="content">
    <div class="sheet">
      <div class="margin-line"></div>
      <ul class="grocery-list">
        <li><span class="box"></span>Milk &amp; eggs</li>
        <li><span class="box"><svg viewBox="0 0 10 10"><path d="M1 5l3 3 5-7" fill="none" stroke="#111" stroke-width="1.8"/></svg></span>Butter</li>
        <li><span class="box"></span>Bread</li>
        <li><span class="box"></span>Vegetables</li>
        <li><span class="box"></span>Shampoo &amp; Conditioner</li>
        <li><span class="box"></span>Frozen peas</li>
        <li><span class="box"></span>Paper towels</li>
        <li><span class="box"></span>Paper bags</li>
        <li><span class="box"></span>Pistachios</li>
        <li><span class="box"></span>Cornstarch</li>
      </ul>
      <div class="index">⌕<br>A<br>B<br>C<br>D<br>E<br>F<br>G<br>H<br>I<br>J<br>K<br>L<br>M<br>N<br>O<br>P<br>Q<br>R<br>S<br>T<br>U<br>V<br>W<br>X<br>Y<br>Z</div>
    </div>
  </div>
  <nav class="tab-bar">
    <span class="tab"><svg viewBox="0 0 12 12" stroke="currentColor" stroke-width="1.4"><path d="M1 3h10M1 6h10M1 9h10"/></svg>List</span>
    <span class="tab tab--active"><svg viewBox="0 0 12 12" fill="none" stroke="currentColor" stroke-width="1.2"><rect x="2" y="2" width="8" height="9"/><path d="M4 7l1.5 1.5L8.5 5"/></svg>Task</span>
    <span class="tab"><svg viewBox="0 0 12 12" fill="none" stroke="currentColor" stroke-width="1.2"><rect x="1.5" y="2.5" width="8" height="8"/><path d="M5 8l.5-1.5L10 2l1 1-4.5 4.5z"/></svg>Notes</span>
    <span class="tab"><svg viewBox="0 0 12 12" fill="none" stroke="currentColor" stroke-width="1.2"><path d="M6 2v8M2 6h8"/></svg>More</span>
  </nav>
</section>

<section class="screen screen--new">
  <div class="status-bar"><span class="carrier">▮▮▮ KESTREL</span><span class="time">0:34</span><span class="battery"><span></span></span></div>
  <header class="nav-bar"><span class="nav-btn nav-btn--back">Back</span><h1 class="nav-title">New task</h1><span class="nav-btn nav-btn--right">Done</span></header>
  <div class="form">
    <div class="task-field">Buy a wedding gift for Tom and Alice<span class="caret"></span></div>
    <div class="form-row form-row--list"><span class="form-label">List</span><span class="form-value">Shopping<span class="chev">›</span></span></div>
    <div class="form-row form-row--who"><span class="form-label">Who</span><span class="form-value">Me<span class="chev">›</span></span></div>
  </div>
  <div class="keyboard">
    <div class="key-row"><span class="key">Q</span><span class="key">W</span><span class="key">E</span><span class="key">R</span><span class="key">T</span><span class="key">Y</span><span class="key">U</span><span class="key">I</span><span class="key">O</span><span class="key">P</span></div>
    <div class="key-row"><span class="key">A</span><span class="key">S</span><span class="key">D</span><span class="key">F</span><span class="key">G</span><span class="key">H</span><span class="key">J</span><span class="key">K</span><span class="key">L</span></div>
    <div class="key-row"><span class="key key--fn">⇧</span><span class="key">Z</span><span class="key">X</span><span class="key">C</span><span class="key">V</span><span class="key">B</span><span class="key">N</span><span class="key">M</span><span class="key key--fn">⌫</span></div>
    <div class="key-row"><span class="key key--fn key--wide">.?123</span><span class="key key--space">space</span><span class="key key--search">Search</span></div>
  </div>
</section>

<section class="screen screen--notes">
  <div class="status-bar"><span class="carrier">▮▮▮ KESTREL</span><span class="time">0:34</span><span class="battery"><span></span></span></div>
  <header class="nav-bar"><h1 class="nav-title">Notes</h1><span class="nav-btn nav-btn--plus">+</span></header>
  <div class="content">
    <div class="notes-sheet">
      <ul class="notes-group">
        <li>My first note<span class="chev">›</span></li>
        <li>My second note<span class="chev">›</span></li>
        <li>My third note<span class="chev">›</span></li>
        <li>My forth note<span class="chev">›</span></li>
        <li class="blank"></li>
      </ul>
    </div>
  </div>
  <nav class="tab-bar">
    <span class="tab"><svg viewBox="0 0 12 12" stroke="currentColor" stroke-width="1.4"><path d="M1 3h10M1 6h10M1 9h10"/></svg>List</span>
    <span class="tab"><svg viewBox="0 0 12 12" fill="none" stroke="currentColor" stroke-width="1.2"><rect x="2" y="2" width="8" height="9"/><path d="M4 7l1.5 1.5L8.5 5"/></svg>Task</span>
    <span class="tab tab--active"><svg viewBox="0 0 12 12" fill="none" stroke="currentColor" stroke-width="1.2"><rect x="1.5" y="2.5" width="8" height="8"/><path d="M5 8l.5-1.5L10 2l1 1-4.5 4.5z"/></svg>Notes</span>
    <span class="tab"><svg viewBox="0 0 12 12" fill="none" stroke="currentColor" stroke-width="1.2"><path d="M6 2v8M2 6h8"/></svg>More</span>
  </nav>
</section>

</body>
</html>
```